New Graphic Design Project

Design a simple and clean PowerPoint slide templates for a Board meeting. The slides should have predominantly white backgrounds and use the brand graphic standards (attached). I'm also attached a PowerPoint master that I don't like, as it's too basic.
The company name is Harbor Lane Gauging.
It sells, calibrates, services and repairs industrial and commercial scales of all types. In particular, Truck scales, floor scales, counting scales and benchtop scales.
The website is harborlanegauging.example but this are the old colors, so ignore the logo and colors. We are launching a new logo and new look. Several variations of the logo are available.

```html
<!DOCTYPE html>
<html lang="en">
<head>
<meta charset="utf-8">
<title>Harbor Lane Gauging — Board of Directors Meeting Q2 2026</title>
<link rel="stylesheet" href="https://fonts.googleapis.com/css2?family=Archivo+Black&family=Inter:wght@400;500;600;700;800&family=Playfair+Display:wght@500&display=swap">
<style>
:root{
  --stage:#3d3d3d;
  --navy:#0b1f4d;
  --navy-2:#1c3360;
  --ink:#1b2f5a;
  --muted:#6f7888;
  --light:#f6f8fb;
  --line:#e3e7ee;
  --orange:#f28c00;
  --green:#1fa36a;
  --row-alt:#d7deeb;
  --sans:'Inter',Arial,sans-serif;
  --display:'Archivo Black','Arial Black',sans-serif;
  --serif:'Playfair Display',Georgia,serif;
}
*{box-sizing:border-box;margin:0;padding:0}
html,body{width:1200px;height:3544px;overflow:hidden}
body{background:var(--stage);font-family:var(--sans);color:var(--ink);position:relative}
.slide{position:absolute;left:102px;width:996px;height:561px;background:#fff;overflow:hidden}
.s1{top:26px;background:var(--navy);color:#fff}
.s2{top:612px}.s3{top:1199px}.s4{top:1785px}.s5{top:2371px}.s6{top:2957px}

/* cover */
.brand{position:absolute;left:75px;top:70px;display:flex;align-items:center;gap:14px}
.brand-mark{width:30px;height:30px;background:var(--orange)}
.brand-name{font-family:var(--display);font-size:24px;letter-spacing:1px;color:#fff}
.cover-title{position:absolute;left:75px;top:220px;font-family:var(--display);font-size:44px;line-height:46px;letter-spacing:.5px}
.cover-rule{position:absolute;left:75px;top:371px;width:92px;height:3px;background:var(--orange)}
.cover-sub{position:absolute;left:75px;top:396px;font-size:19px;font-weight:500}
.cover-lines{position:absolute;left:81px;top:482px;font-size:14px;font-weight:500;letter-spacing:.4px}

/* header & footer */
.slide-title{position:absolute;left:62px;top:40px;font-size:26px;font-weight:500;color:var(--ink)}
.tag{position:absolute;right:62px;top:45px;border:1px solid var(--line);padding:4px 8px;font-size:10px;font-weight:700;letter-spacing:1.6px;color:var(--orange);background:#fffaf2}
.rule{position:absolute;left:62px;right:62px;top:97px;height:6px;background:repeating-linear-gradient(90deg,#c9ced8 0 1px,transparent 1px 5px)}
.foot{position:absolute;left:62px;right:62px;top:502px;border-top:1px solid var(--line);padding-top:12px;display:flex;justify-content:space-between;font-size:8px;letter-spacing:.4px;color:var(--muted)}
.foot b{color:var(--ink);font-weight:700}

/* agenda */
.agenda{position:absolute;left:62px;top:139px;display:flex;gap:16px}
.agenda-card{width:206px;height:296px;background:var(--light);border:1px solid var(--line);padding:26px 20px;position:relative}
.agenda-num{font-family:var(--serif);font-size:24px;color:var(--orange)}
.agenda-num::after{content:"";display:block;width:26px;height:2px;background:var(--ink);margin-top:6px}
.agenda-card h3{font-size:14px;font-weight:500;margin:16px 0 10px}
.agenda-card p{font-size:10px;line-height:18px;color:var(--muted)}
.agenda-time{position:absolute;left:20px;bottom:24px;font-size:8px;font-weight:600}

/* kpis */
.kpis{position:absolute;left:62px;top:124px;display:flex;gap:12px}
.kpi{width:164px;height:85px;border:1px solid var(--line);border-left:3px solid var(--orange);padding:14px 14px}
.kpi-label{font-size:8px;letter-spacing:.3px;color:var(--muted)}
.kpi-value{font-size:25px;font-weight:700;margin:4px 0 1px}
.kpi-note{font-size:9px;color:var(--green)}
.wins{position:absolute;left:62px;right:62px;top:244px;height:184px;background:var(--light);border:1px solid var(--line);padding:18px 24px}
.wins h3{font-size:14px;font-weight:600;display:flex;align-items:center;gap:8px}
.wins-grid{display:grid;grid-template-columns:1fr 1fr;gap:10px 30px;margin-top:10px}
.win{font-size:10.5px;line-height:21px;color:#3c4a66;padding-left:22px;position:relative}
.win::before{content:"✓";position:absolute;left:2px;color:var(--orange);font-weight:700}
.win b{color:var(--ink);font-weight:600}

/* finance */
.chart-box{position:absolute;left:62px;top:135px;width:466px;height:255px;border:1px solid #c9ced8}
.fin-table{position:absolute;left:552px;top:135px;width:382px;border-collapse:collapse;font-size:10px}
.fin-table th{background:var(--navy);color:#fff;font-weight:500;text-align:left;height:30px;padding:0 5px}
.fin-table td{height:31px;padding:0 5px}
.fin-table tr:nth-child(odd) td{background:var(--row-alt)}
.fin-table td:first-child{font-weight:600}
.fin-table .up{color:var(--green)}
.insight{position:absolute;left:552px;top:300px;width:382px;height:90px;background:var(--light);border-left:3px solid var(--navy);padding:12px 14px;font-size:10px;line-height:19px;color:var(--muted)}
.insight h4{font-size:10px;font-weight:600;color:var(--ink)}

/* operations */
.col-head{position:absolute;top:135px;font-size:14px;font-weight:600;border-left:3px solid var(--orange);padding-left:6px;line-height:17px}
.metric{position:absolute;left:62px;width:424px;height:38px;border:1px solid var(--line);border-bottom:none;display:flex;justify-content:space-between;align-items:center;padding:0 16px;font-size:11px}
.metric span:first-child{width:110px;line-height:12px}
.metric .val{color:var(--orange);font-size:15px;font-weight:700}
.initiative{position:absolute;left:510px;width:424px;height:68px;border:1px solid var(--line);display:flex;align-items:center;gap:12px;padding:0 14px}
.init-icon{width:24px;height:24px;border-radius:50%;background:var(--light);border:1px solid var(--line);flex:none;display:grid;place-items:center}
.initiative h4{font-size:11.5px;font-weight:600}
.initiative p{font-size:9.5px;line-height:19px;color:var(--muted)}

/* decisions */
.sub-head{position:absolute;left:62px;font-size:13px;font-weight:600}
.dec-table{position:absolute;left:62px;top:162px;width:489px;border-collapse:collapse;font-size:10px}
.dec-table th{background:var(--navy);color:#fff;font-weight:500;text-align:left;height:30px;padding:0 5px}
.dec-table td{height:30px;padding:0 5px}
.dec-table tr:nth-child(odd) td{background:var(--row-alt)}
.dec-table td:first-child{font-weight:600}
.steps{position:absolute;left:62px;top:334px;list-style:none;font-size:10.5px}
.steps li{height:23px;display:flex;align-items:center;gap:8px}
.box-tick{width:10px;height:10px;border:1px solid var(--orange);display:grid;place-items:center;font-size:8px;color:var(--orange)}
.qa{position:absolute;left:574px;top:135px;width:360px;height:261px;background:var(--navy-2);color:#fff;padding:54px 24px 0;overflow:hidden}
.qa-circle{position:absolute;right:-30px;top:-50px;width:112px;height:112px;border-radius:50%;background:#243c6b}
.qa-square{position:absolute;right:0;bottom:0;width:117px;height:108px;border-radius:26px 26px 0 26px;background:var(--orange)}
.qa h3{font-size:22px;font-weight:500;color:var(--orange);line-height:26px;position:relative}
.qa p{font-size:10px;line-height:18px;color:#c9d2e4;margin-top:10px;width:316px;position:relative}
.qa-sign{position:absolute;left:24px;top:196px;border-top:1px solid #3d5482;padding-top:12px;font-size:8px;width:212px;line-height:11px}
.qa-sign b{display:block;font-weight:700}
.qa-sign span{color:#c9d2e4;letter-spacing:.3px}
</style>
</head>
<body>

<section class="slide s1">
  <div class="brand"><div class="brand-mark"></div><div class="brand-name">HARBOR LANE GAUGING</div></div>
  <h1 class="cover-title">BOARD OF<br>DIRECTORS<br>MEETING</h1>
  <div class="cover-rule"></div>
  <p class="cover-sub">Q2 2026 Business Review</p>
  <p class="cover-lines">SALES • CALIBRATION • SERVICE • REPAIR</p>
</section>

<section class="slide s2">
  <h2 class="slide-title">Board Meeting Agenda</h2>
  <div class="tag">ORDER OF BUSINESS</div>
  <div class="rule"></div>
  <div class="agenda">
    <article class="agenda-card"><div class="agenda-num">01</div><h3>Executive Summary</h3><p>Key highlights, top performance metrics, and a summary of major organizational accomplishments over the last quarter.</p><div class="agenda-time">09:00 AM - 09:30 AM</div></article>
    <article class="agenda-card"><div class="agenda-num">02</div><h3>Financial Performance</h3><p>In-depth analysis of revenue trends, profit margins, operational expenditure, and detailed results by business unit segments.</p><div class="agenda-time">09:30 AM - 10:30 AM</div></article>
    <article class="agenda-card"><div class="agenda-num">03</div><h3>Operations &amp; Service</h3><p>Operational update including critical service delivery times, calibration accuracy scorecards, and customer satisfaction metrics.</p><div class="agenda-time">10:45 AM - 11:30 AM</div></article>
    <article class="agenda-card"><div class="agenda-num">04</div><h3>Strategic Goals</h3><p>Review of ongoing key strategic business initiatives, risk management evaluation, critical board decision points, and next steps.</p><div class="agenda-time">11:30 AM - 12:00 PM</div></article>
  </div>
  <div class="foot"><span>HARBOR LANE GAUGING</span><b>SLIDE 02</b></div>
</section>

<section class="slide s3">
  <h2 class="slide-title">Executive Summary</h2>
  <div class="tag">PERFORMANCE DASHBOARD</div>
  <div class="rule"></div>
  <div class="kpis">
    <div class="kpi"><div class="kpi-label">Q2 REVENUE</div><div class="kpi-value">$4.2M</div><div class="kpi-note">↗ +12% YoY</div></div>
    <div class="kpi"><div class="kpi-label">GROSS MARGIN</div><div class="kpi-value">42%</div><div class="kpi-note">↗ +1.5 bps</div></div>
    <div class="kpi"><div class="kpi-label">SERVICE GROWTH</div><div class="kpi-value">18%</div><div class="kpi-note">↗ Exceeds Target</div></div>
    <div class="kpi"><div class="kpi-label">CUSTOMER RETENTION</div><div class="kpi-value">98%</div><div class="kpi-note">● Industry Leading</div></div>
    <div class="kpi"><div class="kpi-label">NEW ACCOUNTS</div><div class="kpi-value">124</div><div class="kpi-note">↗ +8% Q2 Target</div></div>
  </div>
  <div class="wins">
    <h3><svg width="16" height="14" viewBox="0 0 16 14"><circle cx="5" cy="5" r="4" fill="none" stroke="#f28c00" stroke-width="2"/><circle cx="12" cy="10" r="3" fill="none" stroke="#f28c00" stroke-width="2"/></svg>KEY OPERATIONAL ACCOMPLISHMENTS</h3>
    <div class="wins-grid">
      <p class="win"><b>Expanded calibration service coverage:</b> Successfully deployed advanced mobile calibration units to mid-Atlantic regional territories.</p>
      <p class="win"><b>Increased recurring service contracts:</b> Onboarded 15 new enterprise-level SLA agreements, securing stable long-term recurring revenue streams.</p>
      <p class="win"><b>Improved service response times:</b> Optimized routing and dispatch algorithms, reducing response time for emergency support calls to 4.2 hours.</p>
      <p class="win"><b>Strategic customer acquisition:</b> Added multiple major logistics, pharmaceuticals, and manufacturing accounts to the regional enterprise portfolio.</p>
    </div>
  </div>
  <div class="foot"><span>HARBOR LANE GAUGING • BOARD MEETING PRESENTATION</span><b>SLIDE 03</b></div>
</section>

<section class="slide s4">
  <h2 class="slide-title">Financial Performance</h2>
  <div class="tag">Q2 DATA ANALYSIS</div>
  <div class="rule"></div>
  <div class="chart-box">
    <svg width="466" height="255" viewBox="0 0 466 255" font-family="Inter,Arial,sans-serif">
      <defs><linearGradient id="areaFade" x1="0" y1="0" x2="0" y2="1"><stop offset="0" stop-color="#c9d0dc"/><stop offset="1" stop-color="#c9d0dc" stop-opacity=".1"/></linearGradient></defs>
      <text x="16" y="26" font-size="12" font-weight="600" fill="#1b2f5a">Revenue Trend ($M)</text>
      <circle cx="336" cy="22" r="3" fill="#1b2f5a"/><text x="344" y="25" font-size="8" fill="#1b2f5a">ACTUAL</text>
      <circle cx="394" cy="22" r="3" fill="#f28c00"/><text x="402" y="25" font-size="8" fill="#1b2f5a">FORECAST</text>
      <g stroke="#c9ced8" stroke-width="1"><line x1="52" y1="92" x2="432" y2="92"/><line x1="52" y1="136" x2="432" y2="136"/><line x1="52" y1="180" x2="432" y2="180"/></g>
      <g font-size="8" fill="#6f7888" text-anchor="end"><text x="48" y="95">5.0M</text><text x="48" y="139">3.0M</text><text x="48" y="183">1.0M</text></g>
      <polygon points="138,179 216,171 294,144 373,135 373,182 138,182" fill="url(#areaFade)"/>
      <polyline points="59,204 138,179 216,171 294,144 373,135" fill="none" stroke="#1b2f5a" stroke-width="2"/>
      <line x1="373" y1="135" x2="425" y2="122" stroke="#f28c00" stroke-width="1.5" stroke-dasharray="3 3"/>
      <g fill="#1b2f5a"><circle cx="59" cy="204" r="3"/><circle cx="138" cy="179" r="3"/><circle cx="216" cy="171" r="3"/><circle cx="294" cy="144" r="3"/><circle cx="373" cy="135" r="3"/></g>
      <circle cx="425" cy="122" r="3.5" fill="#f28c00"/>
      <g font-size="8" fill="#6f7888" text-anchor="middle"><text x="59" y="220">Q2-25</text><text x="138" y="220">Q3-25</text><text x="216" y="220">Q4-25</text><text x="294" y="220">Q1-26</text><text x="373" y="220">Q2-26</text><text x="425" y="220" fill="#f28c00">Q3-26 (F)</text></g>
    </svg>
  </div>
  <table class="fin-table">
    <tr><th>Segment</th><th>Revenue</th><th>YoY Growth</th></tr>
    <tr><td>Scale Sales</td><td>$1.8M</td><td class="up">+8%</td></tr>
    <tr><td>Calibration Services</td><td>$1.4M</td><td class="up">+15%</td></tr>
    <tr><td>Service &amp; Repair</td><td>$0.8M</td><td class="up">+22%</td></tr>
    <tr><td>Other/SLA Parts</td><td>$0.2M</td><td class="up">+4%</td></tr>
  </table>
  <div class="insight"><h4>EXECUTIVE KEY INSIGHTS</h4>Overall revenue expanded by 12% driven primarily by calibration services. High SLA margins in Service and Repair continue to favorably shift corporate profitability profiles.</div>
  <div class="foot"><span>HARBOR LANE GAUGING • BOARD MEETING PRESENTATION</span><b>SLIDE 04</b></div>
</section>

<section class="slide s5">
  <h2 class="slide-title">Operations &amp; Growth</h2>
  <div class="tag">STRATEGIC SCORECARD</div>
  <div class="rule"></div>
  <h3 class="col-head" style="left:62px">OPERATIONS PERFORMANCE</h3>
  <h3 class="col-head" style="left:510px">STRATEGIC INITIATIVES</h3>
  <div class="metric" style="top:165px"><span>Service Response Time</span><span class="val">4.2 Hrs</span></div>
  <div class="metric" style="top:210px"><span>First-Time Fix Rate</span><span class="val">92%</span></div>
  <div class="metric" style="top:256px"><span style="width:200px">Calibration Accuracy Index</span><span class="val">99.99%</span></div>
  <div class="metric" style="top:301px"><span>Customer Satisfaction Score</span><span class="val">96%</span></div>
  <div class="initiative" style="top:165px"><div class="init-icon"><svg width="12" height="12" viewBox="0 0 12 12" fill="none" stroke="#1b2f5a" stroke-width="1.3"><path d="M1 1v10h10M3 8l3-3 2 2 3-4"/></svg></div><div><h4>Targeted Market Expansion</h4><p>Expanding direct physical presence into adjacent regional logistics hubs to capture heavy commercial capacity scale operations.</p></div></div>
  <div class="initiative" style="top:245px"><div class="init-icon"><svg width="12" height="12" viewBox="0 0 12 12" fill="#1b2f5a"><circle cx="4" cy="4" r="2"/><circle cx="9" cy="5" r="1.6"/><rect x="1" y="7" width="6" height="4" rx="2"/><rect x="7" y="7.5" width="4" height="3.5" rx="1.5"/></svg></div><div><h4>Operational Excellence &amp; Productivity</h4><p>Automating major back-office dispatch algorithms to boost engineering technician routing efficiency by up to 25%.</p></div></div>
  <div class="initiative" style="top:325px"><div class="init-icon"><svg width="12" height="12" viewBox="0 0 12 12" fill="none" stroke="#1b2f5a" stroke-width="1.3"><rect x="1.5" y="2" width="9" height="6"/><path d="M0.5 10h11"/></svg></div><div><h4>Technological Integration</h4><p>Deploying advanced end-to-end digital field portals to enable seamless and paperless calibration report generation.</p></div></div>
  <div class="foot"><span>HARBOR LANE GAUGING • BOARD MEETING PRESENTATION</span><b>SLIDE 05</b></div>
</section>

<section class="slide s6">
  <h2 class="slide-title">Next Steps &amp; Decisions</h2>
  <div class="tag">BOARD ACTION REQUIRED</div>
  <div class="rule"></div>
  <h3 class="sub-head" style="top:137px">KEY DECISIONS &amp; APPROVALS REQUIRED</h3>
  <table class="dec-table">
    <tr><th>Decision Topic</th><th>Owner</th><th>Target Date</th></tr>
    <tr><td>Regional Expansion Capital</td><td>CEO / CFO</td><td>July 15, 2026</td></tr>
    <tr><td>Strategic SLA Pricing Update</td><td>Head of Ops</td><td>August 1, 2026</td></tr>
    <tr><td>Q3 Regional Service Budget</td><td>Full Board</td><td>July 30, 2026</td></tr>
  </table>
  <h3 class="sub-head" style="top:311px;font-size:12px">NEXT STEPS</h3>
  <ul class="steps">
    <li><span class="box-tick">✓</span>Formally approve corporate growth investment capital allocations</li>
    <li><span class="box-tick">✓</span>Finalize tactical operational implementation plan</li>
    <li><span class="box-tick">✓</span>Schedule next strategic quarterly performance assessment</li>
  </ul>
  <aside class="qa">
    <div class="qa-circle"></div>
    <div class="qa-square"></div>
    <h3>Questions &amp;<br>Discussion</h3>
    <p>Open forum for executive directors, shareholders, and operating advisors. Thank you for your continued trust and strategic stewardship.</p>
    <div class="qa-sign"><b>Harbor Lane Gauging</b><span>Industrial Weighing Services</span></div>
  </aside>
  <div class="foot"><span>HARBOR LANE GAUGING • BOARD MEETING PRESENTATION</span><b>SLIDE 06</b></div>
</section>

</body>
</html>
```